Auto glass company

BRIGHTWAY
Roving Auto Glass, LLC
555-604-1937

* Windshield Replacement
* Rock Chip Repair
Danny "K"
Brightwayrovingautoglass@example.com
* Fully Insured

This is what I would like on the card. The image is what I had before. Looking for a logo possible too, couldn’t find a place to add that on. It’s a auto glass company.

Target Market(s)

Auto glass

Industry/Entity Type

Auto glass

Contact Information for Business Card

Logo, business name, phone number, windshield replacement, rock chip repair, insured, owner name Danny K, email address brightwayrovingautoglass@example.com

Colors

Designer to choose colors to be used in the design.

Requirements
Must have
• Logo, business name, phone number, windshield replacement, rock chip repair, insured, owner name Danny K, email address brightwayrovingautoglass@example.com

```html
<!DOCTYPE html>
<html lang="en">
<head>
<meta charset="utf-8">
<title>Brightway Roving Auto Glass – Business Card</title>
<link rel="stylesheet" href="https://fonts.googleapis.com/css2?family=Tenor+Sans&family=Lato:wght@700&display=swap">
<style>
  :root {
    --page-bg: #e4e6e9;
    --card-white: #ffffff;
    --card-shade: #e9eaec;
    --ink: #3a3d42;
    --ink-soft: #55595f;
    --brand-blue: #1767a6;
    --band-dark: #0e4f86;
    --band-light: #6cc3ee;
    --silver: #c9cdd2;
  }
  * { box-sizing: border-box; margin: 0; padding: 0; }
  html, body { width: 1200px; height: 900px; overflow: hidden; }
  body {
    background: var(--page-bg);
    font-family: "Tenor Sans", sans-serif;
    color: var(--ink);
    position: relative;
  }
  .card {
    position: absolute;
    left: 270px;
    width: 660px;
    height: 377px;
    background: linear-gradient(110deg, var(--card-shade) 0%, var(--card-white) 45%, var(--card-white) 75%, #f1f2f4 100%);
    box-shadow: 0 10px 28px rgba(0,0,0,.22);
    overflow: hidden;
  }
  .card--front { top: 52px; }
  .card--back { top: 471px; }

  .card__band {
    position: absolute;
    left: 0; right: 0; bottom: 0;
    height: 26px;
    border-top: 4px solid var(--silver);
    background: linear-gradient(90deg, var(--band-dark) 0%, #1a6fae 30%, var(--band-light) 55%, #1a6fae 72%, var(--band-dark) 100%);
  }

  .brand {
    position: absolute;
    top: 44px;
    right: 46px;
    display: flex;
    align-items: center;
    gap: 14px;
    color: var(--ink);
  }
  .brand__dot {
    width: 16px; height: 16px;
    border-radius: 50%;
    background: var(--brand-blue);
  }
  .brand__text { line-height: 1; }
  .brand__name {
    display: block;
    font-size: 44px;
    letter-spacing: 1px;
  }
  .brand__sub {
    display: block;
    font-size: 18px;
    letter-spacing: 3px;
    margin-top: 6px;
  }

  .services {
    position: absolute;
    left: 58px;
    bottom: 70px;
    list-style: none;
    font-size: 21px;
    color: var(--ink-soft);
  }
  .services li {
    display: flex;
    align-items: center;
    gap: 12px;
    margin-top: 6px;
  }
  .services svg { width: 18px; height: 18px; fill: var(--brand-blue); flex: none; }

  .contact {
    position: absolute;
    left: 58px;
    bottom: 62px;
  }
  .contact__name {
    font-family: "Lato", sans-serif;
    font-weight: 700;
    font-size: 30px;
    color: var(--brand-blue);
    margin-bottom: 20px;
  }
  .contact__line {
    display: flex;
    align-items: center;
    gap: 12px;
    font-size: 21px;
    color: var(--ink-soft);
    margin-top: 6px;
  }
  .contact__line svg { width: 18px; height: 18px; flex: none; }
</style>
</head>
<body>

  <section class="card card--front" aria-label="Card front">
    <div class="brand">
      <span class="brand__dot"></span>
      <span class="brand__text">
        <span class="brand__name">BRIGHTWAY</span>
        <span class="brand__sub">Roving Auto Glass, LLC</span>
      </span>
    </div>
    <ul class="services">
      <li><svg viewBox="0 0 20 20"><path d="M10 0 12.5 7.5 20 10 12.5 12.5 10 20 7.5 12.5 0 10 7.5 7.5Z"/></svg>Fully Insured</li>
      <li><svg viewBox="0 0 20 20"><path d="M10 0 12.5 7.5 20 10 12.5 12.5 10 20 7.5 12.5 0 10 7.5 7.5Z"/></svg>Rock Chip Repair</li>
      <li><svg viewBox="0 0 20 20"><path d="M10 0 12.5 7.5 20 10 12.5 12.5 10 20 7.5 12.5 0 10 7.5 7.5Z"/></svg>Windshield Replacement</li>
    </ul>
    <div class="card__band"></div>
  </section>

  <section class="card card--back" aria-label="Card back">
    <div class="brand">
      <span class="brand__dot"></span>
      <span class="brand__text">
        <span class="brand__name">BRIGHTWAY</span>
        <span class="brand__sub">Roving Auto Glass, LLC</span>
      </span>
    </div>
    <div class="contact">
      <p class="contact__name">Danny "K"</p>
      <p class="contact__line">
        <svg viewBox="0 0 20 20" fill="none" stroke="#1767a6" stroke-width="1.8"><rect x="5" y="1.5" width="10" height="17" rx="2"/><line x1="9" y1="15.5" x2="11" y2="15.5"/></svg>
        555-604-1937
      </p>
      <p class="contact__line">
        <svg viewBox="0 0 20 20"><path d="M2 8 10 2 18 8V18H2Z" fill="#1767a6"/><path d="M2 8 10 13 18 8" fill="none" stroke="#fff" stroke-width="1.5"/></svg>
        brightwayrovingautoglass@example.com
      </p>
    </div>
    <div class="card__band"></div>
  </section>

</body>
</html>
```